Brighter Than Dawn Home Entertainment

We are a home Brighter Than Dawn Home Entertainment focus on front projection system and home theater surround system. We built highend home theater for people to enjoy movie, sports and gaming on big screen at home.
I'm looking for a dispaly to showcase our work as well as help people build their home theater

Number of Pages Required

3 page

Colors

Designer to choose colors to be used in the design.

Requirements
Must have
• Home Page
• What we do
• Who we are
• Gallery
• Contact Us
Nice to have
• Picture jump out of big screen make a 3D feeling

```html
<!DOCTYPE html>
<html lang="en">
<head>
<meta charset="utf-8">
<title>Brighter Than Dawn Home Entertainment</title>
<link href="https://fonts.googleapis.com/css2?family=Fredoka:wght@500;600&family=Source+Sans+3:wght@300;400&family=Roboto+Condensed:wght@400;700&display=swap" rel="stylesheet">
<style>
:root{
  --gold:#a88a43;
  --gold-soft:#b99d5c;
  --gold-deep:#8b7031;
  --ink:#1c1c1c;
  --band:#f7f7f7;
  --white:#ffffff;
}
*{box-sizing:border-box;margin:0;padding:0}
html,body{width:1200px;height:3015px;overflow:hidden;background:var(--white)}
body{position:relative;font-family:"Source Sans 3",sans-serif;color:var(--gold)}
.abs{position:absolute}
.photo{position:absolute}

.band-hero{left:0;top:0;width:1200px;height:660px;background:var(--band)}
.band-who{left:0;top:1146px;width:1200px;height:1220px;background:var(--band)}

.brand{left:117px;top:20px;display:flex;align-items:center;gap:12px;font-family:"Fredoka",sans-serif;font-weight:500;font-size:18px;line-height:1.1;color:var(--ink);width:300px}
.brand-mark{width:22px;height:22px;background:var(--ink);flex:none}
.nav{left:655px;top:22px;display:flex;gap:28px;font-family:"Fredoka",sans-serif;font-weight:600;font-size:10px;letter-spacing:1px}
.nav a{color:var(--gold);text-decoration:none;padding-bottom:5px}
.nav a.active{border-bottom:1.5px solid var(--gold)}
.search{left:1120px;top:8px}

.hero-title{left:200px;top:100px;width:330px;text-align:right;font-family:"Fredoka",sans-serif;font-weight:500;font-size:72px;line-height:70px;color:var(--gold);letter-spacing:-1px}
.hero-frame{left:671px;top:175px;width:268px;height:340px;border:1.5px solid var(--gold)}
.hero-photo{left:549px;top:275px;width:360px;height:292px;background:linear-gradient(135deg,#3a3a3a,#0e0e0e 60%,#2a2a2a)}
.scroll-btn{left:372px;top:503px;width:60px;height:62px;border:1.5px solid var(--gold);display:flex;align-items:center;justify-content:center}

.h2{font-family:"Source Sans 3",sans-serif;font-weight:400;font-size:44px;color:var(--gold);line-height:1}
.body-copy{font-size:13.5px;line-height:26px;font-weight:300;color:var(--gold-soft)}
.body-copy p+p{margin-top:4px}
.more{font-size:13px;color:var(--gold);border-bottom:1.5px solid var(--gold);padding-bottom:3px}

.do-photo{left:209px;top:748px;width:203px;height:306px;background:linear-gradient(90deg,#1a1a1a,#4a4a4a 30%,#111 50%,#3d3d3d 75%,#151515)}
.do-title{left:422px;top:772px}
.do-copy{left:478px;top:888px;width:570px}

.who-title{left:287px;top:1228px}
.who-frame{left:301px;top:1383px;width:226px;height:340px;border:1.5px solid var(--gold)}
.who-photo{left:253px;top:1412px;width:256px;height:283px;background:linear-gradient(160deg,#cfd8e8,#6f86ad 40%,#f2f2f2 60%,#cfcfcf)}
.who-copy{left:579px;top:1488px;width:466px}
.who-more{left:981px;top:1690px}

.gal-title{left:241px;top:1806px}
.gal-copy{left:255px;top:1924px;width:456px}
.gal-more{left:253px;top:2128px}
.gal-frame{left:770px;top:1819px;width:229px;height:342px;border:1.5px solid var(--gold)}
.gal-photo{left:790px;top:1773px;width:255px;height:368px;background:linear-gradient(110deg,#eef0f7,#b5b8c8 35%,#1c1c1c 55%,#2b2b2b)}
.cable-photo{left:253px;top:2178px;width:382px;height:226px;background:radial-gradient(closest-side,rgba(47,73,184,.85),rgba(91,112,207,.45) 60%,rgba(247,247,247,0))}
.plus{left:575px;top:2231px}

.contact-title{left:285px;top:2420px;font-family:"Roboto Condensed",sans-serif;font-weight:700;font-size:27px;color:var(--gold);letter-spacing:.5px}
.partner{left:836px;top:2446px;display:flex;align-items:center;gap:10px;font-family:"Source Sans 3",sans-serif;font-weight:400;font-size:22px;line-height:1.1;color:var(--ink);width:220px}
.partner-mark{width:16px;height:16px;background:var(--ink);flex:none}

.studio-photo{left:0;top:2512px;width:880px;height:503px;background:linear-gradient(180deg,#f4f4f4 0%,#e4e4e4 55%,#d6d6d6 100%)}
.studio-card{left:297px;top:2532px;width:356px;height:246px;background:#efefef;padding:22px 24px;font-family:"Roboto Condensed",sans-serif}
.studio-card h3{font-weight:700;font-size:19px;letter-spacing:1px;color:#6e5a2a;margin-bottom:18px}
.studio-line{display:flex;gap:14px;font-size:17px;line-height:34px;color:var(--gold-deep)}
.studio-line svg{flex:none;margin-top:8px}
</style>
</head>
<body>
<div class="abs band-hero"></div>
<div class="abs band-who"></div>

<header>
  <div class="abs brand"><span class="brand-mark"></span>Brighter Than Dawn Home Entertainment</div>
  <nav class="abs nav">
    <a class="active" href="#about">ABOUT</a>
    <a href="#products">PRODUCTS</a>
    <a href="#projects">PROJECTS</a>
    <a href="#contact">CONTACT</a>
  </nav>
  <svg class="abs search" width="26" height="26" viewBox="0 0 26 26" fill="none" stroke="#a88a43" stroke-width="2"><circle cx="11" cy="11" r="7"/><line x1="16" y1="16" x2="23" y2="23"/></svg>
</header>

<section id="about">
  <h1 class="abs hero-title">Life is<br>real<br>life is<br>earnest</h1>
  <div class="abs hero-frame"></div>
  <div class="photo hero-photo" role="img" aria-label="Close-up of a black tower speaker with round drivers"></div>
  <div class="abs scroll-btn">
    <svg width="18" height="12" viewBox="0 0 18 12" fill="none" stroke="#a88a43" stroke-width="2"><polyline points="2,2 9,9 16,2"/></svg>
  </div>
</section>

<section id="what-we-do">
  <div class="photo do-photo" role="img" aria-label="Pair of black floor-standing speakers"></div>
  <h2 class="abs h2 do-title">What we do</h2>
  <div class="abs body-copy do-copy">
    <p>We design and install front projection systems and surround sound rooms that bring the cinema into your home.</p>
    <p>Every room is tuned for movies, sports and gaming on a big screen. From wiring to calibration, our team handles the full build with care.</p>
  </div>
</section>

<section id="who-we-are">
  <h2 class="abs h2 who-title">Who we are</h2>
  <div class="abs who-frame"></div>
  <div class="photo who-photo" role="img" aria-label="Large flat screen with a surround speaker set"></div>
  <div class="abs body-copy who-copy">
    <p>A small team of installers and sound engineers who love the big screen experience and want to share it with every family.</p>
    <p>Since our start we have built private theaters in homes of every size, planning screens, seating, acoustics and lighting so each room feels like ...</p>
  </div>
  <a class="abs more who-more">read more</a>

  <h2 class="abs h2 gal-title">Gallery</h2>
  <div class="abs body-copy gal-copy">
    <p>Take a look inside the rooms we have finished, from compact media lounges to full cinema spaces with tiered seating, acoustic panels, hidden speakers, projection screens and custom lighting that sets the mood for every film night at home ...</p>
  </div>
  <a class="abs more gal-more">read more</a>
  <div class="abs gal-frame"></div>
  <div class="photo gal-photo" role="img" aria-label="Slim black speaker column beside a wall screen"></div>
  <div class="photo cable-photo" role="img" aria-label="Blue network cable plug"></div>
  <svg class="abs plus" width="48" height="48" viewBox="0 0 48 48" stroke="#a88a43" stroke-width="1.5"><line x1="24" y1="0" x2="24" y2="48"/><line x1="0" y1="24" x2="48" y2="24"/></svg>
</section>

<section id="contact">
  <h2 class="abs contact-title">CONTAKT</h2>
  <div class="abs partner"><span class="partner-mark"></span>Northlight Home Viewing</div>

  <div class="photo studio-photo" role="img" aria-label="Living room with a television on a white media stand, a house plant and a speaker"></div>

  <div class="abs studio-card">
    <h3>OUR STUDIO</h3>
    <div class="studio-line">
      <svg width="16" height="20" viewBox="0 0 16 20" fill="none" stroke="#8b7031" stroke-width="1.6"><path d="M8 19s6-6.5 6-11A6 6 0 0 0 2 8c0 4.5 6 11 6 11z"/><circle cx="8" cy="8" r="2.2"/></svg>
      <span>Ruko Sinar Blok 7 No.4 - 5, Jl. Lintas Cahaya, Kota Baru 10990 - Indonesia</span>
    </div>
    <div class="studio-line" style="margin-top:14px">
      <svg width="16" height="18" viewBox="0 0 16 18" fill="none" stroke="#8b7031" stroke-width="1.6"><path d="M3 1l3 4-2 2c1 3 3 5 6 6l2-2 3 3-2 3C7 17 0 10 1 3z"/></svg>
      <span>(+62) 21-5550 1470</span>
    </div>
  </div>
</section>
</body>
</html>
```